Talvick Industrial Maintenance Business Card

Design a business card with the following information, logo must be included.
Talvick Industrial Maintenance
Dan Pelfrey Jr.
Pone 555-214-7608
email dan.pelfrey.jr@mailvantor.com

```html
<!DOCTYPE html>
<html lang="en">
<head>
<meta charset="UTF-8">
<title>Talvick Industrial Maintenance – Business Card</title>
<link href="https://fonts.googleapis.com/css2?family=Montserrat:wght@400;500;700;800&display=swap" rel="stylesheet">
<style>
  :root {
    --brand-blue: #1572b9;
    --ink-grey: #5a5a5a;
    --rule-grey: #8a8a8a;
    --paper: #ffffff;
    --backdrop: #5e5e60;
  }
  * { box-sizing: border-box; margin: 0; padding: 0; }
  html, body { width: 1200px; height: 780px; overflow: hidden; }
  body {
    background: var(--backdrop);
    font-family: "Montserrat", sans-serif;
    display: flex;
    align-items: center;
    justify-content: center;
    gap: 50px;
  }
  .card {
    position: relative;
    width: 525px;
    height: 300px;
    background: var(--paper);
    overflow: hidden;
    box-shadow: 0 10px 24px rgba(0,0,0,.35);
  }
  .band {
    position: absolute;
    left: 0;
    width: 100%;
    height: 84px;
    background: var(--brand-blue);
  }
  .card-front .band { top: 0; }
  .card-back .band { bottom: 0; }

  .brand {
    display: flex;
    align-items: center;
    gap: 10px;
    color: var(--brand-blue);
    font-weight: 700;
    text-transform: uppercase;
  }
  .brand-dot {
    flex: none;
    border-radius: 50%;
    background: var(--brand-blue);
  }
  .brand-name { line-height: 1.05; }

  .card-front .brand {
    position: absolute;
    top: 112px;
    left: 0;
    width: 100%;
    justify-content: center;
  }
  .card-front .brand-dot { width: 46px; height: 46px; }
  .card-front .brand-name { font-size: 26px; }
  .card-front .brand-name small { display: block; font-size: 12.5px; letter-spacing: .6px; }

  .site {
    position: absolute;
    left: 50px;
    right: 50px;
    top: 200px;
    border-top: 1px solid var(--rule-grey);
    border-bottom: 1px solid var(--rule-grey);
    padding: 12px 0;
    text-align: center;
    font-size: 10.5px;
    letter-spacing: 3.2px;
    color: var(--ink-grey);
  }

  .card-back .brand {
    position: absolute;
    top: 26px;
    right: 34px;
    gap: 7px;
  }
  .card-back .brand-dot { width: 26px; height: 26px; }
  .card-back .brand-name { font-size: 13px; }
  .card-back .brand-name small { display: block; font-size: 6.5px; letter-spacing: .3px; }

  .person {
    position: absolute;
    left: 36px;
    top: 88px;
    width: 290px;
    padding-bottom: 10px;
    border-bottom: 1px solid var(--rule-grey);
  }
  .person-name {
    font-size: 27px;
    font-weight: 800;
    color: var(--brand-blue);
    line-height: 1.1;
  }
  .person-title {
    font-size: 10px;
    letter-spacing: 1px;
    color: var(--ink-grey);
    text-transform: uppercase;
    margin-top: 2px;
  }
  .contacts {
    position: absolute;
    left: 44px;
    top: 162px;
    list-style: none;
    font-size: 12px;
    color: var(--ink-grey);
  }
  .contacts li { display: flex; align-items: center; gap: 9px; margin-bottom: 8px; }
  .contacts svg { width: 13px; height: 13px; fill: var(--brand-blue); flex: none; }
</style>
</head>
<body>

<section class="card card-front" aria-label="Card front">
  <div class="band"></div>
  <div class="brand">
    <span class="brand-dot"></span>
    <span class="brand-name">Talvick<small>Industrial Maintenance</small></span>
  </div>
  <p class="site">www.talvickindustrialmaintenance.com</p>
</section>

<section class="card card-back" aria-label="Card back">
  <div class="brand">
    <span class="brand-dot"></span>
    <span class="brand-name">Talvick<small>Industrial Maintenance</small></span>
  </div>
  <div class="person">
    <h1 class="person-name">Dan Pelfrey Jr.</h1>
    <p class="person-title">Managing Director</p>
  </div>
  <ul class="contacts">
    <li>
      <svg viewBox="0 0 24 24" aria-hidden="true"><path d="M6.6 10.8a15 15 0 0 0 6.6 6.6l2.2-2.2a1 1 0 0 1 1-.25 11.4 11.4 0 0 0 3.6.57 1 1 0 0 1 1 1V20a1 1 0 0 1-1 1A17 17 0 0 1 3 4a1 1 0 0 1 1-1h3.5a1 1 0 0 1 1 1c0 1.25.2 2.45.57 3.57a1 1 0 0 1-.25 1z"/></svg>
      555-214-7608
    </li>
    <li>
      <svg viewBox="0 0 24 24" aria-hidden="true"><path d="M2 5h20v14H2z M2 5l10 8 10-8" fill="none" stroke="#1572b9" stroke-width="2"/><path d="M3 6l9 7 9-7v12H3z"/></svg>
      dan.pelfrey.jr@mailvantor.com
    </li>
  </ul>
  <div class="band"></div>
</section>

</body>
</html>
```